Flyers for social media company

To create a postcard sized flyer to send to potential clients informing them of our business and what we can offer.

We are a social media company offering clients web design, social media management on a number of platforms.

Would be nice to have our Northgate surrounded by a number of yellow ducks so the blue stand out from the crowd.

Business

```html
<!DOCTYPE html>
<html lang="en">
<head>
<meta charset="UTF-8">
<title>Northgate – Social Media Management</title>
<link href="https://fonts.googleapis.com/css2?family=Montserrat:wght@400;600;700;800&display=swap" rel="stylesheet">
<style>
  :root {
    --brand-blue: #2aa2e8;
    --ink: #111111;
    --paper: #ffffff;
    --bar-dark: #2b2b2b;
    --photo-dark: #1d2330;
    --photo-mid: #4a3f5c;
    --photo-warm: #a5453e;
  }
  * { margin: 0; padding: 0; box-sizing: border-box; }
  html, body { width: 800px; height: 1200px; overflow: hidden; background: var(--paper); }
  body { font-family: "Montserrat", Arial, sans-serif; color: var(--ink); }

  .flyer { position: relative; width: 800px; height: 1200px; background: var(--paper); }

  .hero-photo {
    position: absolute; left: 0; top: 0; width: 800px; height: 582px;
    background:
      radial-gradient(circle at 20% 25%, rgba(230,90,60,0.55), transparent 35%),
      radial-gradient(circle at 80% 20%, rgba(220,70,90,0.5), transparent 30%),
      radial-gradient(circle at 70% 75%, rgba(70,120,200,0.45), transparent 35%),
      linear-gradient(160deg, var(--photo-warm) 0%, var(--photo-mid) 40%, var(--photo-dark) 100%);
  }

  .hero-name {
    position: absolute; left: 0; top: 232px; width: 800px; text-align: center;
    font-weight: 800; font-size: 82px; line-height: 1; letter-spacing: 2px;
    color: var(--paper);
  }

  .about { position: absolute; left: 0; top: 600px; width: 800px; text-align: center; }
  .about-title { font-weight: 700; font-size: 56px; letter-spacing: 2px; line-height: 1; }
  .about-rule { width: 610px; height: 3px; background: var(--ink); margin: 14px auto 0; }
  .about-text {
    width: 620px; margin: 16px auto 0; text-align: left;
    font-size: 23px; line-height: 1.22;
  }

  .services { position: absolute; left: 0; top: 793px; width: 800px; height: 190px; }
  .service { position: absolute; width: 220px; text-align: center; }
  .service:nth-child(1) { left: 52px; }
  .service:nth-child(2) { left: 287px; }
  .service:nth-child(3) { left: 525px; }
  .service-icon {
    width: 114px; height: 114px; border-radius: 50%; background: var(--brand-blue);
    margin: 0 auto; display: flex; align-items: center; justify-content: center;
  }
  .service-label { margin-top: 12px; font-size: 27px; line-height: 1.05; }

  .slogan {
    position: absolute; left: 0; top: 1008px; width: 800px; text-align: center;
    font-weight: 700; font-size: 31px;
  }

  .contact-bar {
    position: absolute; left: 90px; top: 1064px; width: 625px; height: 114px;
    background: var(--bar-dark); border-radius: 22px;
    display: flex; align-items: center; color: var(--paper);
  }
  .contact-dot {
    width: 54px; height: 54px; margin-left: 30px; border-radius: 50%;
    background: var(--brand-blue); flex: none;
  }
  .contact-brand-name {
    margin-left: 18px; font-weight: 800; font-size: 38px; line-height: 1; letter-spacing: 0.5px;
  }
  .contact-divider { width: 3px; height: 62px; background: var(--paper); margin: 0 22px; flex: none; }
  .contact-phone { font-weight: 700; font-size: 30px; line-height: 1; }
  .contact-cta { font-weight: 600; font-size: 15px; letter-spacing: 0.8px; margin-top: 6px; }
</style>
</head>
<body>
<main class="flyer">
  <div class="hero-photo" role="img" aria-label="Close-up photo of a smartphone screen full of colourful social media app icons"></div>

  <p class="hero-name">NORTHGATE</p>

  <section class="about">
    <h1 class="about-title">ABOUT US</h1>
    <div class="about-rule"></div>
    <p class="about-text">We are a social networking company that offers web design and social network administration services on several platforms.</p>
  </section>

  <section class="services">
    <div class="service">
      <div class="service-icon">
        <svg width="66" height="60" viewBox="0 0 66 60" fill="none" stroke="#fff" stroke-width="4" stroke-linejoin="round" stroke-linecap="round">
          <rect x="4" y="6" width="44" height="32" rx="3"/>
          <line x1="26" y1="38" x2="26" y2="48"/>
          <line x1="16" y1="50" x2="36" y2="50"/>
          <rect x="50" y="28" width="12" height="20" rx="6"/>
          <line x1="56" y1="28" x2="56" y2="35"/>
        </svg>
      </div>
      <div class="service-label">Excellent<br>services</div>
    </div>
    <div class="service">
      <div class="service-icon">
        <svg width="50" height="66" viewBox="0 0 50 66" fill="none" stroke="#fff" stroke-width="4" stroke-linejoin="round" stroke-linecap="round">
          <path d="M25 4a19 19 0 0 0-11 34.5c2 1.6 3 4 3 6.5v3h16v-3c0-2.5 1-4.9 3-6.5A19 19 0 0 0 25 4z"/>
          <line x1="17" y1="54" x2="33" y2="54"/>
          <line x1="19" y1="61" x2="31" y2="61"/>
        </svg>
      </div>
      <div class="service-label">A lot of<br>creativity</div>
    </div>
    <div class="service">
      <div class="service-icon">
        <svg width="62" height="62" viewBox="0 0 62 62" fill="none" stroke="#fff" stroke-width="4" stroke-linejoin="round" stroke-linecap="round">
          <circle cx="31" cy="31" r="26"/>
          <polyline points="18,32 27,41 44,22"/>
        </svg>
      </div>
      <div class="service-label">Customer<br>satisfaction</div>
    </div>
  </section>

  <p class="slogan">We are your best alternative</p>

  <footer class="contact-bar">
    <div class="contact-dot"></div>
    <div class="contact-brand-name">NORTHGATE</div>
    <div class="contact-divider"></div>
    <div class="contact-details">
      <div class="contact-phone">1-800-555-0148</div>
      <div class="contact-cta">CONTACT US</div>
    </div>
  </footer>
</main>
</body>
</html>
```